Plumquill.media

I need a full page PSD made (desktop and mobile view) with a layout similar to what I have in my text file, but a smooth flowing, good looking design. Only take my text file as an idea of order things show flow. I have taken my exact steps from the text file, put them together, and it did not look good, which is why I am seeking a professional design.

```html
<!DOCTYPE html>
<html lang="en">
<head>
<meta charset="utf-8">
<title>Plumquill.media — 5 Star Reviews and Text Message Marketing</title>
<link rel="stylesheet" href="https://fonts.googleapis.com/css2?family=Mulish:ital,wght@0,300;0,400;0,600;0,700;0,800;1,400&display=swap">
<style>
:root{
  --blue:#1a6fd8;
  --blue-dark:#1565c8;
  --ink:#2b3a55;
  --muted:#8a94a6;
  --page:#f4f8fe;
  --hero:#e2eefc;
  --soft:#dbe6f3;
  --card:#f3f5f8;
  --footer:#e7eef9;
  --white:#ffffff;
}
*{box-sizing:border-box;margin:0;padding:0}
html,body{width:1200px;height:3536px;overflow:hidden}
body{font-family:"Mulish",sans-serif;background:var(--page);color:var(--ink);position:relative}
.abs{position:absolute}
.hero-bg{position:absolute;left:0;top:0;width:1200px;height:640px}
.logo{position:absolute;font-weight:800;font-size:20px;color:var(--ink);letter-spacing:-.3px;display:flex;align-items:center;gap:6px}
.logo .dot{width:8px;height:8px;background:var(--blue);border-radius:50%}
.nav a{position:absolute;top:30px;font-size:12px;font-weight:600;color:var(--blue);text-decoration:none}
.nav .login{color:var(--ink);font-size:10px;top:33px}
.btn-signin{position:absolute;left:890px;top:25px;width:68px;height:26px;background:var(--blue);color:#fff;font-size:10px;font-weight:700;border-radius:3px;display:flex;align-items:center;justify-content:center;box-shadow:0 4px 10px rgba(26,111,216,.3)}
h1.hero-title{position:absolute;left:242px;top:205px;font-size:37px;line-height:43px;font-weight:800;color:var(--ink)}
.hero-sub{position:absolute;left:247px;top:310px;font-size:19px;font-weight:300;color:var(--ink)}
.btn-primary{position:absolute;background:var(--blue);color:#fff;font-weight:700;display:flex;align-items:center;justify-content:center;gap:8px;box-shadow:0 10px 24px rgba(26,111,216,.3)}
.photo{position:absolute;border-radius:6px}
.t-card{position:absolute;background:var(--white);border-radius:8px;box-shadow:0 8px 22px rgba(43,58,85,.1);display:flex;align-items:center;padding-left:20px;gap:12px}
.t-card .avatar{width:36px;height:36px;border-radius:50%;background:linear-gradient(135deg,#c79b80,#5a3b2e);flex:none}
.t-card .name{font-size:12px;font-weight:800;color:var(--ink)}
.t-card .role{font-size:8px;color:var(--muted)}
.t-quote{position:absolute;background:var(--soft);border-radius:8px;display:flex;align-items:center;padding-left:16px;gap:14px;font-size:10px;font-style:italic;color:var(--muted);line-height:15px}
.t-quote .qm{font-size:36px;font-weight:800;color:var(--ink);font-style:italic;line-height:1;margin-top:14px}
.section-title{position:absolute;left:0;width:1200px;text-align:center;font-size:30px;font-weight:800;color:var(--ink)}
.section-sub{position:absolute;left:0;width:1200px;text-align:center;font-size:14px;color:var(--muted)}
.step-no{position:absolute;font-size:14px;color:var(--muted)}
.step-title{position:absolute;font-size:30px;line-height:37px;font-weight:800;color:var(--ink)}
.step-desc{position:absolute;font-size:14px;line-height:19px;color:var(--muted)}
.link{position:absolute;font-size:12px;font-weight:800;color:var(--blue)}
.offer-card{position:absolute;left:240px;top:953px;width:280px;height:192px;border-radius:12px;overflow:hidden;box-shadow:0 16px 34px rgba(43,58,85,.18);display:flex}
.offer-card .img{width:136px;height:100%;background:linear-gradient(160deg,#8b939c,#3d444c 60%,#6a727b)}
.offer-card .txt{flex:1;background:#d4dae2;display:flex;flex-direction:column;align-items:center;justify-content:center;font-weight:600;color:var(--ink);text-align:center}
.chat{position:absolute;left:604px;top:1314px;width:209px;height:290px;background:#fff;padding:10px 8px;font-size:7px;line-height:9px}
.bubble-in{background:#e6e6ea;border-radius:10px;padding:8px 10px;color:#222;margin-bottom:6px}
.bubble-out{background:#1e8bf6;color:#fff;border-radius:8px;padding:4px 8px;margin:0 0 6px 118px}
.bubble-in a{color:#1a6fd8;text-decoration:underline}
.review-card{position:absolute;left:242px;top:1760px;width:278px;height:187px;border-radius:12px;background:#8eb4f2;overflow:hidden;box-shadow:0 16px 34px rgba(43,58,85,.14)}
.review-card .paper{position:absolute;left:12px;top:24px;right:12px;bottom:0;background:#fff;text-align:center;padding-top:16px}
.stars{color:#f39a1e;font-size:13px;letter-spacing:3px;margin-top:6px}
.marketing{position:absolute;left:242px;top:2229px;width:716px;height:388px;box-shadow:0 20px 40px rgba(26,111,216,.2)}
.marketing .panel{position:absolute;left:0;top:0;width:435px;height:388px;background:var(--blue);color:#fff;padding:50px 0 0 72px;font-size:16px;line-height:25px;font-weight:400}
.marketing .panel p{margin-bottom:27px}
.marketing .phone{position:absolute;left:435px;top:0;width:281px;height:388px;background:linear-gradient(150deg,#e4e8ee,#c8ced6 55%,#4f5761)}
.price-card{position:absolute;top:2859px;width:204px;height:313px;background:#eaf2fd;text-align:center}
.price-card.featured{background:linear-gradient(#d9e8fb,#c8dcf8);box-shadow:0 20px 40px rgba(26,111,216,.15)}
.price-card h3{font-size:14px;font-weight:400;color:var(--muted);margin-top:30px}
.price-card.featured h3{color:var(--ink)}
.price{margin-top:12px;color:var(--ink);font-weight:800;font-size:30px;line-height:30px}
.price sup{font-size:12px;font-weight:400;vertical-align:14px}
.price small{font-size:14px;font-weight:400}
.contract{font-size:9px;color:var(--muted);margin-top:2px}
.features{list-style:none;text-align:left;margin:18px 0 0 22px;font-size:11px;color:var(--muted)}
.price-card.featured .features{color:var(--ink)}
.features li{height:25px;display:flex;align-items:center;gap:6px}
.features svg{width:10px;height:10px;flex:none}
.plan-btn{position:absolute;top:3172px;width:205px;height:43px;border:1px solid var(--blue);color:var(--blue);font-size:12px;font-weight:800;display:flex;align-items:center;justify-content:center;gap:8px;background:transparent}
.plan-btn.solid{background:var(--blue);color:#fff;box-shadow:0 12px 24px rgba(26,111,216,.35)}
footer{position:absolute;left:0;top:3286px;width:1200px;height:250px;background:var(--footer);text-align:center}
footer .f-text{font-size:14px;color:var(--muted)}
</style>
</head>
<body>

<svg class="hero-bg" viewBox="0 0 1200 640" aria-hidden="true">
  <path d="M0 0H1200V430C1120 440 1050 470 970 520C880 575 760 630 640 615C520 600 430 540 300 540C170 540 80 530 0 530Z" fill="#e2eefc"/>
</svg>

<header class="nav">
  <div class="logo" style="left:242px;top:22px">Plumquill.media<span class="dot"></span></div>
  <a href="#" style="left:562px">Home</a>
  <a href="#" style="left:625px">Pricing</a>
  <a href="#" style="left:693px">Contact</a>
  <a href="#" class="login" style="left:842px">LOGIN</a>
  <div class="btn-signin">Sign In</div>
</header>

<section class="hero">
  <h1 class="hero-title">Get 5 Star reviews and<br>Text message Marketing</h1>
  <div class="hero-sub">All in one tool!</div>
  <div class="btn-primary" style="left:243px;top:394px;width:205px;height:43px;font-size:12px">Get Started <span>›</span></div>
  <div class="photo" role="img" aria-label="Photo of a smiling man with a tablet in front of bookshelves" style="left:752px;top:125px;width:388px;height:312px;background:linear-gradient(135deg,#d9dde3 0%,#a6b7cc 45%,#5c7ea8 75%,#e8eaee 100%);box-shadow:0 16px 40px rgba(43,58,85,.15)"></div>
  <div class="t-card" style="left:707px;top:313px;width:251px;height:44px">
    <div class="avatar" role="img" aria-label="Profile photo"></div>
    <div><div class="name">Lena Marsh</div><div class="role">Marketing Director</div></div>
  </div>
  <div class="t-quote" style="left:707px;top:364px;width:251px;height:44px"><span class="qm">“</span>Would recommend to friends &amp; family.</div>
</section>

<h2 class="section-title" style="top:700px">How it Works</h2>
<div class="section-sub" style="top:748px">5 Star Review System</div>

<svg class="abs" style="left:130px;top:870px" width="420" height="360" aria-hidden="true">
  <path d="M250 10C330 20 360 120 350 190C340 270 260 340 170 335C80 330 10 270 8 200C5 120 60 90 110 60C160 30 200 5 250 10Z" fill="#d3e4fb" opacity=".85"/>
</svg>
<div class="t-card" style="left:73px;top:850px;width:252px;height:44px">
  <div class="avatar" role="img" aria-label="Profile photo"></div>
  <div><div class="name">Nora P.</div><div class="role">Sales Manager</div></div>
</div>
<div class="t-quote" style="left:73px;top:900px;width:252px;height:45px"><span class="qm">“</span>Plumquill media was worth a fortune<br>to my company.</div>

<div class="offer-card">
  <div class="img" role="img" aria-label="Photo of a shop cash register counter"></div>
  <div class="txt"><div style="font-size:14px;line-height:18px">Get 50% OFF<br>Your Order!</div><div style="font-size:17px;line-height:23px;margin-top:18px">Text VIP to<br>482917</div></div>
</div>

<div class="step-no" style="left:606px;top:965px">Step #1</div>
<div class="step-title" style="left:606px;top:986px">Star Review System</div>
<div class="step-desc" style="left:606px;top:1034px">You display an offer near your cash register.</div>
<div class="link" style="left:605px;top:1095px">Get Started &nbsp;›</div>

<div class="step-no" style="left:242px;top:1285px">Step #2</div>
<div class="step-title" style="left:242px;top:1305px">Customer starts the<br>review sequence.</div>
<div class="step-desc" style="left:242px;top:1392px">Only 5 star responses are directed to your<br>review link. 1-4 star responses are asked to<br>reply with feedback.</div>
<div class="link" style="left:241px;top:1492px">Get Started &nbsp;›</div>
<div class="t-card" style="left:242px;top:1534px;width:252px;height:45px">
  <div class="avatar" role="img" aria-label="Profile photo"></div>
  <div><div class="name">Owen T.</div><div class="role">Sales Consultant</div></div>
</div>
<div class="t-quote" style="left:242px;top:1586px;width:252px;height:45px"><span class="qm">“</span>I don't know what else to say.<br>Thank You!</div>

<div class="chat">
  <div class="bubble-in">Thank you for being a valued customer. This will only take a minute!<br><br>One a scale of 1 to 5, how many stars would you rate our establishment?<br><br>Please reply with a number.</div>
  <div class="bubble-out">5</div>
  <div class="bubble-in">Thank you! Can you take 1 minute to leave us a review on the link below?<br><br><a>http://www.reviewlink.example/Store</a><br><br>When you are finished, please reply with the word "Done" to receive your 50% off.</div>
  <div class="bubble-out">done</div>
  <div class="bubble-in">You're Awesome! Please show this message to the cashier and mention the discount.</div>
</div>

<div class="review-card">
  <div class="paper">
    <div style="font-size:11px;color:#222">Congrats! You got a 5-star review</div>
    <div class="stars">★★★★★</div>
    <div style="font-size:6px;line-height:8px;color:#333;margin:6px 22px 0">"Great people who will take the time to help you They go above and beyond Will be back One very happy..."</div>
    <div style="width:18px;height:18px;border-radius:50%;background:#6f96e6;margin:12px auto 0"></div>
    <div style="font-size:5px;color:#777;margin-top:2px">Reviewed by<br>Local Guide</div>
    <div style="width:148px;height:16px;background:#3c7cea;margin:8px auto 0;color:#fff;font-size:6px;line-height:16px;font-weight:700">READ REVIEW</div>
    <div style="display:flex;justify-content:space-around;align-items:center;font-size:5px;color:#555;margin-top:10px">
      <span>Learn more</span><span style="width:44px;height:12px;background:#111;border-radius:2px"></span><span>Ask an expert</span>
    </div>
  </div>
</div>

<div class="step-no" style="left:607px;top:1715px">Step #3</div>
<div class="step-title" style="left:607px;top:1736px">Your business earns<br>5 star reviews!</div>
<div class="link" style="left:606px;top:1851px">Get Started &nbsp;›</div>
<div class="t-card" style="left:607px;top:1895px;width:253px;height:44px">
  <div class="avatar" role="img" aria-label="Profile photo"></div>
  <div><div class="name">Felix R.</div><div class="role">Sales Consultant</div></div>
</div>
<div class="t-quote" style="left:607px;top:1947px;width:253px;height:44px"><span class="qm">“</span>Thanks for the great service.</div>

<h2 class="section-title" style="top:2098px">How it Works</h2>
<div class="section-sub" style="top:2145px">Text Marketing System</div>

<div class="marketing">
  <div class="panel">
    <p>#1 &nbsp;Phone numbers are collected from<br>Cash Register Offer.</p>
    <p>#2 &nbsp;Simply log into the dashboard and<br>send all your customers a text message<br>of any specials or promotions.</p>
    <p>#3 &nbsp;Watch your customer come<br>through the door!</p>
    <div style="font-size:13px;font-weight:800;margin-top:10px">Get Started &nbsp;›</div>
  </div>
  <div class="phone" role="img" aria-label="Photo of a phone showing a text from Sprinkle Lane Donuts: Today only we're offering a buy one get one free donut special"></div>
</div>

<h2 class="section-title" style="top:2724px">Pricing</h2>
<div class="section-sub" style="top:2773px">Simple Price. All the Benefits.</div>

<div class="price-card" style="left:279px">
  <h3>Basic Package</h3>
  <div class="price"><sup>$</sup>89<small>/mo</small></div>
  <div class="contract">No Contract</div>
  <ul class="features">
    <li><svg viewBox="0 0 10 10"><path d="M1 5l3 3 5-6" stroke="#8a94a6" stroke-width="1.8" fill="none"/></svg>Lorem Ipsum Dolos Itam</li>
    <li><svg viewBox="0 0 10 10"><path d="M1 5l3 3 5-6" stroke="#8a94a6" stroke-width="1.8" fill="none"/></svg>Consectetur Adipisicing</li>
    <li><svg viewBox="0 0 10 10"><path d="M1 5l3 3 5-6" stroke="#8a94a6" stroke-width="1.8" fill="none"/></svg>Seddo Eiusmod Temp</li>
    <li><svg viewBox="0 0 10 10"><path d="M1 5l3 3 5-6" stroke="#8a94a6" stroke-width="1.8" fill="none"/></svg>Incididunt Utabore</li>
    <li><svg viewBox="0 0 10 10"><path d="M1 5l3 3 5-6" stroke="#8a94a6" stroke-width="1.8" fill="none"/></svg>Commodo Consequat</li>
  </ul>
</div>
<div class="price-card featured" style="left:498px">
  <h3>Ultimate Package</h3>
  <div class="price"><sup>$</sup>149<small>/mo</small></div>
  <div class="contract">No Contract</div>
  <ul class="features">
    <li><svg viewBox="0 0 10 10"><path d="M1 5l3 3 5-6" stroke="#2b3a55" stroke-width="1.8" fill="none"/></svg>Customer Review System</li>
    <li><svg viewBox="0 0 10 10"><path d="M1 5l3 3 5-6" stroke="#2b3a55" stroke-width="1.8" fill="none"/></svg>Text Message Marketing</li>
    <li><svg viewBox="0 0 10 10"><path d="M1 5l3 3 5-6" stroke="#2b3a55" stroke-width="1.8" fill="none"/></svg>Customer Feedback</li>
    <li><svg viewBox="0 0 10 10"><path d="M1 5l3 3 5-6" stroke="#2b3a55" stroke-width="1.8" fill="none"/></svg>Email Notifications</li>
    <li><svg viewBox="0 0 10 10"><path d="M1 5l3 3 5-6" stroke="#2b3a55" stroke-width="1.8" fill="none"/></svg>Online Dashboard</li>
  </ul>
</div>
<div class="price-card" style="left:717px">
  <h3>Pro Package</h3>
  <div class="price"><sup>$</sup>109<small>/mo</small></div>
  <div class="contract">No Contract</div>
  <ul class="features">
    <li><svg viewBox="0 0 10 10"><path d="M1 5l3 3 5-6" stroke="#8a94a6" stroke-width="1.8" fill="none"/></svg>Lorem Ipsum Dolos Itam</li>
    <li><svg viewBox="0 0 10 10"><path d="M1 5l3 3 5-6" stroke="#8a94a6" stroke-width="1.8" fill="none"/></svg>Consectetur Adipisicing</li>
    <li><svg viewBox="0 0 10 10"><path d="M1 5l3 3 5-6" stroke="#8a94a6" stroke-width="1.8" fill="none"/></svg>Seddo Eiusmod Temp</li>
    <li><svg viewBox="0 0 10 10"><path d="M1 5l3 3 5-6" stroke="#8a94a6" stroke-width="1.8" fill="none"/></svg>Incididunt Utabore</li>
    <li><svg viewBox="0 0 10 10"><path d="M1 5l3 3 5-6" stroke="#8a94a6" stroke-width="1.8" fill="none"/></svg>Commodo Consequat</li>
  </ul>
</div>
<div class="plan-btn" style="left:279px">Select Plan <span>›</span></div>
<div class="plan-btn solid" style="left:498px">Get Started <span>›</span></div>
<div class="plan-btn" style="left:717px">Select Plan <span>›</span></div>

<footer>
  <div class="logo" style="left:0;width:1200px;justify-content:center;top:70px;font-size:22px">Plumquill.media<span class="dot"></span></div>
  <div class="f-text abs" style="left:0;width:1200px;top:133px">Copyright©2020 Plumquill.media</div>
  <div class="f-text abs" style="left:0;width:1200px;top:166px">All Rights Reserved</div>
</footer>

</body>
</html>
```